I'm looking for an app for customers to order through

I'm looking for an app for my customers to order products through
Ideally each customer would have a customer number with password
Their profile would come up with a preloaded products they currently order
From there they can select the product they require and volume needed for delivery
I would also like an option for them to go to a full product range if they are looking for Ideas or a product they don't currently use
Once the order is completed a copy of the order is them e-mailed to my distribution facilities and a confirmation sent to the customer by e-mail and/or SMS
Current product list is approx 1000 items
Current customers is 80 with expectations to expand to 200
On average current products ordered by each customer is is between 4-8 items
Ordering units are done by both weight and pieces/units

Target Market(s)

Food service outlets,
Restaurant , Hotels, catering companies, clubs, take away shops, cafes
Retail outlets

Number of Pages Required

1 page

Font styles to use
Sans Serif

Colors
abd037

Requirements
Must have
• Customer log in with Password 4 - 6 digit
• Customer order history
Nice to have
• Area for promotions / specials on a weekly / monthly basis

```html
<!DOCTYPE html>
<html lang="en">
<head>
<meta charset="utf-8">
<title>Verdant Pantry – Menu</title>
<link rel="stylesheet" href="https://fonts.googleapis.com/css2?family=Raleway:wght@300;400;700&display=swap">
<style>
  :root {
    --brand: #abd037;
    --panel: #a8d46c;
    --tile: #8cc640;
    --row: rgba(255, 255, 255, 0.16);
    --ink: #1f2a12;
    --white: #ffffff;
  }
  * { box-sizing: border-box; margin: 0; padding: 0; }
  html, body { width: 1200px; height: 1120px; overflow: hidden; background: #ffffff; }
  body { position: relative; font-family: "Raleway", sans-serif; color: var(--ink); }

  .app-screen {
    position: absolute; left: 370px; top: 120px; width: 462px; height: 820px;
    background: var(--panel); overflow: hidden;
  }
  .backdrop {
    position: absolute; inset: 0;
    background:
      radial-gradient(ellipse 60% 35% at 70% 70%, rgba(120, 150, 60, 0.35), transparent 70%),
      radial-gradient(ellipse 50% 30% at 85% 50%, rgba(235, 245, 215, 0.55), transparent 70%),
      linear-gradient(180deg, #a8d46c 0%, #b6db84 40%, #c9e4a6 75%, #d8ebbf 100%);
  }

  .app-header { position: absolute; left: 0; top: 0; width: 100%; height: 100px; }
  .menu-toggle { position: absolute; left: 24px; top: 40px; }
  .brand { position: absolute; left: 117px; top: 23px; display: flex; align-items: center; gap: 8px; }
  .brand-mark { width: 60px; height: 60px; border-radius: 50%; background: var(--white); }
  .brand-name {
    font-weight: 700; font-size: 24px; line-height: 23px; color: var(--ink);
    text-transform: uppercase; letter-spacing: 0.5px;
  }
  .search-button { position: absolute; left: 417px; top: 43px; }

  .category {
    position: absolute; left: 24px; width: 412px; height: 65px;
    background: var(--row);
  }
  .category.is-open { height: 220px; }
  .category-icon {
    position: absolute; left: 0; top: 0; width: 65px; height: 65px;
    background: var(--tile); display: flex; align-items: center; justify-content: center;
    box-shadow: 1px 1px 3px rgba(0,0,0,0.12);
  }
  .category-title {
    position: absolute; left: 98px; top: 16px;
    font-weight: 400; font-size: 26px; line-height: 32px; color: var(--ink);
  }
  .category-arrow { position: absolute; right: 26px; top: 26px; }
  .category.is-open .category-arrow { top: 30px; right: 24px; }

  .sub-list { position: absolute; left: 98px; top: 62px; list-style: none; }
  .sub-list li {
    position: relative; padding-left: 17px; height: 39.5px;
    font-size: 20px; line-height: 24px; font-weight: 400; color: #2a3a18;
  }
  .sub-list li::before {
    content: ""; position: absolute; left: 2px; top: 8px;
    border-left: 4px solid var(--white); border-top: 4px solid transparent; border-bottom: 4px solid transparent;
  }
</style>
</head>
<body>
<main class="app-screen">
  <div class="backdrop" role="img" aria-label="Soft blurred photograph of fresh green leaves"></div>

  <header class="app-header">
    <svg class="menu-toggle" width="36" height="24" viewBox="0 0 36 24">
      <rect x="0" y="0" width="36" height="4" fill="#fff"/>
      <rect x="0" y="10" width="30" height="4" fill="#fff"/>
      <rect x="0" y="20" width="26" height="4" fill="#fff"/>
    </svg>
    <div class="brand">
      <span class="brand-mark"></span>
      <span class="brand-name">Verdant<br>Pantry</span>
    </div>
    <svg class="search-button" width="22" height="22" viewBox="0 0 22 22">
      <circle cx="8.5" cy="8.5" r="6" fill="none" stroke="#fff" stroke-width="3"/>
      <line x1="13" y1="13" x2="20" y2="20" stroke="#fff" stroke-width="4" stroke-linecap="round"/>
    </svg>
  </header>

  <section class="category is-open" style="top:106px">
    <div class="category-icon">
      <svg width="40" height="40" viewBox="0 0 40 40"><circle cx="20" cy="20" r="17" fill="none" stroke="#fff" stroke-width="3"/><circle cx="14" cy="15" r="2" fill="#fff"/><circle cx="23" cy="12" r="2" fill="#fff"/><circle cx="26" cy="22" r="2" fill="#fff"/><circle cx="16" cy="26" r="2" fill="#fff"/><circle cx="21" cy="20" r="1.5" fill="#fff"/></svg>
    </div>
    <h2 class="category-title">Snacks</h2>
    <svg class="category-arrow" width="14" height="8" viewBox="0 0 14 8"><path d="M0 0h14L7 8z" fill="#fff"/></svg>
    <ul class="sub-list">
      <li>Your Heading</li>
      <li>Your Heading</li>
      <li>Your Heading</li>
      <li>Your Heading</li>
    </ul>
  </section>

  <section class="category" style="top:341px">
    <div class="category-icon">
      <svg width="44" height="40" viewBox="0 0 44 40"><path d="M6 16h32v18a4 4 0 0 1-4 4H10a4 4 0 0 1-4-4z" fill="#fff"/><path d="M6 16l16-10 16 10z" fill="#fff"/><rect x="6" y="22" width="32" height="2" fill="#8cc640"/><rect x="6" y="29" width="32" height="2" fill="#8cc640"/></svg>
    </div>
    <h2 class="category-title">Dessert</h2>
    <svg class="category-arrow" width="8" height="14" viewBox="0 0 8 14"><path d="M0 0l8 7-8 7z" fill="#fff"/></svg>
  </section>

  <section class="category" style="top:419px">
    <div class="category-icon">
      <svg width="44" height="44" viewBox="0 0 44 44"><path d="M4 22h36v8a10 10 0 0 1-10 10H14A10 10 0 0 1 4 30z" fill="#fff"/><circle cx="14" cy="20" r="5" fill="#fff"/><circle cx="22" cy="18" r="6" fill="#fff"/><line x1="28" y1="20" x2="33" y2="4" stroke="#fff" stroke-width="3"/><line x1="33" y1="20" x2="39" y2="5" stroke="#fff" stroke-width="3"/></svg>
    </div>
    <h2 class="category-title">Chinese</h2>
    <svg class="category-arrow" width="8" height="14" viewBox="0 0 8 14"><path d="M0 0l8 7-8 7z" fill="#fff"/></svg>
  </section>

  <section class="category" style="top:497px">
    <div class="category-icon">
      <svg width="40" height="44" viewBox="0 0 40 44"><path d="M6 24h28l-4 18H10z" fill="#fff"/><path d="M5 24c0-8 6-14 15-14s15 6 15 14z" fill="#fff"/><circle cx="20" cy="7" r="5" fill="#fff"/><path d="M6 28q7 4 14 0q7 4 14 0" fill="none" stroke="#8cc640" stroke-width="2"/></svg>
    </div>
    <h2 class="category-title">Cake</h2>
    <svg class="category-arrow" width="8" height="14" viewBox="0 0 8 14"><path d="M0 0l8 7-8 7z" fill="#fff"/></svg>
  </section>

  <section class="category" style="top:576px">
    <div class="category-icon">
      <svg width="46" height="46" viewBox="0 0 46 46"><path d="M3 16h40a20 16 0 0 1-40 0z" fill="#fff"/><line x1="15" y1="30" x2="9" y2="44" stroke="#fff" stroke-width="3"/><line x1="31" y1="30" x2="37" y2="44" stroke="#fff" stroke-width="3"/><line x1="16" y1="4" x2="16" y2="11" stroke="#fff" stroke-width="3"/><line x1="23" y1="2" x2="23" y2="11" stroke="#fff" stroke-width="3"/><line x1="30" y1="4" x2="30" y2="11" stroke="#fff" stroke-width="3"/></svg>
    </div>
    <h2 class="category-title">B,B,Q</h2>
    <svg class="category-arrow" width="8" height="14" viewBox="0 0 8 14"><path d="M0 0l8 7-8 7z" fill="#fff"/></svg>
  </section>

  <section class="category" style="top:654px">
    <div class="category-icon">
      <svg width="46" height="46" viewBox="0 0 46 46"><rect x="3" y="24" width="40" height="4" rx="2" fill="#fff"/><path d="M6 30h34a17 10 0 0 1-34 0z" fill="#fff"/><rect x="14" y="42" width="18" height="3" fill="#fff"/><path d="M20 21c-4-4 4-7 0-12" fill="none" stroke="#fff" stroke-width="2.5"/><line x1="28" y1="22" x2="40" y2="8" stroke="#fff" stroke-width="3.5" stroke-linecap="round"/></svg>
    </div>
    <h2 class="category-title">Soup</h2>
    <svg class="category-arrow" width="8" height="14" viewBox="0 0 8 14"><path d="M0 0l8 7-8 7z" fill="#fff"/></svg>
  </section>

  <section class="category" style="top:732px">
    <div class="category-icon">
      <svg width="40" height="40" viewBox="0 0 40 40"><path d="M20 2l5.3 12 13 1.2-9.8 8.7 2.9 12.8L20 30l-11.4 6.7 2.9-12.8-9.8-8.7 13-1.2z" fill="#fff"/></svg>
    </div>
    <h2 class="category-title">Today Special</h2>
    <svg class="category-arrow" width="8" height="14" viewBox="0 0 8 14"><path d="M0 0l8 7-8 7z" fill="#fff"/></svg>
  </section>

  <section class="category" style="top:808px">
    <div class="category-icon"></div>
  </section>
</main>
</body>
</html>
```